Post it Note design

POST-IT NOTE DESIGN (CONTENT)
Size recommended: 4x6 for handwriting space.
Header (Bold):
Lighting Issue Detected on Your Property
Sub-header:
During our routine night inspection, we noted the following item(s):
Checkbox List:
⬜ Building Lights Out
⬜ Pole Lights Out
⬜ Sign Not Illuminated
⬜ Other ________________________
Action Line:
We can provide a quote or dispatch service right away.
Area for notes
Contact Block (Bold & Centered):
Brovane Fixture Inc.
Service@BrovaneFixture.com
www.BrovaneFixture.com
877-514-0862
Industry/Entity Type
Electrical lighting
Colors
Designer to choose colors to be used in the design.
Look and feel
Each slider illustrates characteristics of the customer's brand and the style your logo design should communicate.

```html
<!DOCTYPE html>
<html lang="en">
<head>
<meta charset="utf-8">
<title>Brovane Fixture Inc. – Lighting Issue Notice</title>
<link href="https://fonts.googleapis.com/css2?family=Montserrat:wght@400;500;600;700;800;900&display=swap" rel="stylesheet">
<style>
  :root {
    --red: #ec1c24;
    --navy: #283583;
    --ink: #1a1a1a;
    --panel: #ececec;
    --panel-edge: #8a8a8a;
    --paper: #ffffff;
    --backdrop: #e6e6e6;
  }
  * { margin: 0; padding: 0; box-sizing: border-box; }
  html, body { width: 1200px; height: 1200px; overflow: hidden; }
  body {
    background: var(--backdrop);
    font-family: "Montserrat", sans-serif;
    position: relative;
  }
  .note {
    position: absolute;
    left: 233px; top: 50px;
    width: 734px; height: 1100px;
    background: var(--paper);
  }
  .note > * { position: absolute; }

  .brand-name {
    top: 58px; left: 0; width: 100%;
    text-align: center;
    color: var(--red);
    font-weight: 800;
    font-size: 62px;
    line-height: 1.1;
    letter-spacing: 1px;
    text-transform: uppercase;
  }

  .alert-band {
    top: 239px; left: 0; width: 100%; height: 133px;
    background: var(--red);
    border-top: 5px solid var(--navy);
    border-bottom: 5px solid var(--navy);
    display: flex; align-items: center; justify-content: center;
    text-align: center;
    color: #fff;
    font-weight: 800;
    font-size: 44px;
    line-height: 1.08;
    word-spacing: 6px;
    text-shadow: 2px 2px 3px rgba(0,0,0,.45);
  }

  .intro {
    top: 385px; left: 0; width: 100%;
    text-align: center;
    color: var(--navy);
    font-size: 25px;
    line-height: 1.15;
    font-weight: 500;
  }
  .intro strong { font-weight: 700; }

  .checklist {
    top: 465px; left: 161px; width: 388px; height: 214px;
    background: var(--panel);
    border: 1.5px solid var(--panel-edge);
    border-radius: 14px;
    list-style: none;
    padding: 12px 0 0 20px;
  }
  .checklist li {
    display: flex; align-items: center;
    height: 48.5px;
    color: var(--navy);
    font-weight: 600;
    font-size: 30px;
    white-space: nowrap;
  }
  .checkbox {
    width: 28px; height: 27px;
    border: 2px solid #333;
    background: #fff;
    margin-right: 15px;
    flex: none;
  }
  .blank-line {
    display: inline-block;
    width: 216px;
    border-bottom: 2px solid var(--navy);
    height: 26px;
  }

  .service-offer {
    top: 707px; left: 89px; width: 544px; height: 97px;
    background: var(--navy);
    border-radius: 12px;
    color: #fff;
    text-align: center;
    text-shadow: 1px 2px 3px rgba(0,0,0,.5);
    padding-top: 3px;
  }
  .service-offer .small { font-size: 22px; font-weight: 600; line-height: 1.1; letter-spacing: -.5px; }
  .service-offer .big { font-size: 41px; font-weight: 900; line-height: 1.1; }

  .notes { left: 43px; width: 638px; }
  .notes .line { display: flex; align-items: flex-end; height: 42px; }
  .notes .label { font-size: 21px; font-weight: 500; color: var(--ink); margin-right: 4px; }
  .notes .dots { flex: 1; border-bottom: 3px dotted var(--ink); margin-bottom: 4px; }
  .notes { top: 814px; }
  .notes .line + .line { height: 44px; }

  .contact-name {
    top: 944px; left: 0; width: 100%;
    text-align: center;
    color: var(--navy);
    font-weight: 800;
    font-size: 40px;
    word-spacing: 10px;
    text-transform: uppercase;
  }
  .contact-phone {
    top: 990px; left: 0; width: 100%;
    display: flex; justify-content: center; align-items: center; gap: 6px;
    color: var(--red);
    font-weight: 800;
    font-size: 50px;
  }
  .contact-phone svg { width: 32px; height: 38px; }
  .contact-web {
    top: 1050px; left: 0; width: 100%;
    text-align: center;
    color: var(--ink);
    font-size: 17px;
    font-weight: 500;
  }
  .contact-web .accent { color: var(--navy); }

  .footer-stripe {
    top: 1087px; left: 0; width: 100%; height: 13px;
    display: flex; gap: 3px;
  }
  .footer-stripe span { flex: 1; }
  .footer-stripe .red { background: var(--red); }
  .footer-stripe .navy { background: var(--navy); }
</style>
</head>
<body>
  <main class="note">
    <div class="brand-name">Brovane<br>Fixture Inc.</div>

    <h1 class="alert-band">LIGHTING ISSUE DETECTED<br>ON YOUR PROPERTY</h1>

    <p class="intro">During our <strong>routine night inspection,</strong> we noted<br>the following item(s):</p>

    <ul class="checklist">
      <li><span class="checkbox"></span>Building Lights Out</li>
      <li><span class="checkbox"></span>Sign Not Illuminated</li>
      <li><span class="checkbox"></span>Pole Lights Out</li>
      <li><span class="checkbox"></span>Other<span class="blank-line"></span></li>
    </ul>

    <div class="service-offer">
      <div class="small">WE CAN PROVIDE A</div>
      <div class="big">QUOTE OR DISPATCH</div>
      <div class="small">SERVICE RIGHT AWAYS</div>
    </div>

    <div class="notes">
      <div class="line"><span class="label">NOTES</span><span class="dots"></span></div>
      <div class="line"><span class="dots"></span></div>
      <div class="line"><span class="dots"></span></div>
    </div>

    <div class="contact-name">Brovane Fixture Inc.</div>
    <div class="contact-phone">
      <svg viewBox="0 0 32 38" aria-hidden="true">
        <path d="M7 3 L12 2 L15 11 L11 14 Q12 22 18 27 L22 24 L29 30 L26 35 Q18 38 10 28 Q3 18 7 3 Z" fill="#283583"/>
        <path d="M19 8 Q25 10 26 17 M20 3 Q29 6 30 16" stroke="#283583" stroke-width="2" fill="none"/>
      </svg>
      <span>877-514-0862</span>
    </div>
    <div class="contact-web">service@BrovaneFixture.com | www.<span class="accent">BrovaneFixture</span>.com</div>

    <div class="footer-stripe"><span class="red"></span><span class="navy"></span></div>
  </main>
</body>
</html>
```